Fahrzeugbeschriftung für Darmtherapie und Kurspraxis
Zielgruppe
Kurspraxis Sonnenstunde Velmar. die Kurspraxis, Workshops, (siehe Flyer). und holistische Darmtherapie fröhlich vital marlene kostka
Diese Beklebung soll dazu dienen, die Reichweite von Sonnenstunde Velmar und Fröhlich vital zu erhöhen und potenzielle Kunden auf die Dienstleistungen aufmerksam zu machen.
sonnenstunde: https://www.sonnenstunde-velmar.de
Adresse:** Lindenkampweg 84, Oberhausen
Beschreibung: sonnenstunde ist ein Ort, der Familien verbindet. Das Unternehmen bietet ein breites Spektrum an Kursen für alle Altersgruppen an, von Schwimmkursen über Yoga bis hin zu Rückbildungskursen. Darüber hinaus bietet sonnenstunde einen Ort des Austauschs und eine Gemeinschaft für Gleichgesinnte.
- Fröhlich vital Marlene Kostka: Darmtherapie für Frauen, Mamas und Frauen mit Kinderwunsch: https://www.froehlich-vital-marlene-kostka.de
-Beschreibung: Marlene Kostka bietet eine Darmtherapie an, die darauf abzielt, das Immunsystem ganzheitlich zu regulieren und bei hormonellem Ungleichgewicht zu helfen. Diese Therapie ist auch für Babys und Kinder geeignet und kann zu mehr Kraft, reguliertem Hormonhaushalt und einem neuen Lebensgefühl führen.
Zielgruppe:
Die Zielgruppe für die Autobeklebung umfasst Eltern, Familien und Frauen, die auf der Suche nach ganzheitlichen Gesundheitslösungen sind. Dies schließt sowohl Menschen ein, die nach Kursen und Gemeinschaft suchen (sonnenstunde), als auch solche, die Interesse an Darmtherapien haben (Fröhlich vital Marlene Kostka).
4. Ziele der Autobeklebung:
- Erhöhung der Sichtbarkeit und Bekanntheit der beiden Unternehmen
- Ansprache der Zielgruppe während des täglichen Verkehrs
- Vermittlung von Informationen über die angebotenen Dienstleistungen und Kurse
**5. Designvorschläge:**
- Die Beklebung sollte auffällig sein (bitte nicht zu bunt )und das Logo sowie die Kontaktdaten beider Unternehmen klar darstellen.
Aufgabenstellung
eyecather Kundengewinnung. (hatte schon an einen kackhaufen gedacht, aber das mag ich nicht). nicht zu bunt. ist ein grauer N6 (Pure Grey, Raven-Sandwick/Raven-Sandwick/Raven). . nur die Scheiben sollen beklebt werden, maximal etwas über die Scheiben. Seitenscheiben und Heckscheibe. Die Heckscheibe (hatte ich schonmal in Waben Folie Komplett. Von innen kann man raus schauen. Von außen nicht rein)

```html
<!DOCTYPE html>
<html lang="de">
<head>
<meta charset="utf-8">
<title>Fahrzeugbeschriftung – Fröhlich vital &amp; Sonnenstunde</title>
<link rel="stylesheet" href="https://fonts.googleapis.com/css2?family=Poppins:wght@300;500;600;700&family=Roboto:wght@500&family=Libre+Baskerville&display=swap">
<style>
  :root {
    --page: #ffffff;
    --teal: #93cfcf;
    --teal-deep: #7fc3c4;
    --olive: #c4bc3c;
    --olive-light: #d4cc5a;
    --lavender: #b7b5e6;
    --lavender-soft: #cfcdf1;
    --ink-soft: #55557a;
    --white: #ffffff;
  }
  html, body {
    margin: 0;
    width: 1200px;
    height: 676px;
    overflow: hidden;
    background: var(--page);
  }
  .window-wrap {
    position: absolute;
    left: 50px;
    top: 169px;
    width: 1100px;
    height: 337px;
  }
  .window-wrap svg { display: block; width: 100%; height: 100%; }
  .brand-kicker { font-family: "Poppins", sans-serif; font-weight: 500; font-size: 19px; letter-spacing: 1.2px; fill: var(--white); }
  .brand-name { font-family: "Poppins", sans-serif; font-weight: 700; font-size: 27px; letter-spacing: .4px; fill: var(--white); }
  .brand-role { font-family: "Poppins", sans-serif; font-weight: 600; font-size: 7.4px; letter-spacing: 1.1px; fill: var(--white); }
  .brand-phone { font-family: "Roboto", sans-serif; font-weight: 500; font-size: 23px; fill: var(--white); }
  .brand-web { font-family: "Roboto", sans-serif; font-weight: 500; font-size: 11px; letter-spacing: 1.6px; fill: var(--white); }
  .offer-label { font-family: "Poppins", sans-serif; font-weight: 500; font-size: 7px; fill: var(--ink-soft); }
  .practice-name { font-family: "Poppins", sans-serif; font-weight: 300; font-size: 27px; letter-spacing: .5px; fill: var(--white); }
  .practice-tagline { font-family: "Libre Baskerville", serif; font-size: 15px; fill: var(--white); }
  .practice-intro { font-family: "Poppins", sans-serif; font-weight: 600; font-size: 6.4px; fill: var(--white); }
  .practice-contact { font-family: "Poppins", sans-serif; font-weight: 500; font-size: 10.8px; fill: var(--white); }
</style>
</head>
<body>
<div class="window-wrap">
  <svg viewBox="0 0 800 245" xmlns="http://www.w3.org/2000/svg" aria-label="Seitenscheiben-Beklebung">
    <defs>
      <clipPath id="window-shape">
        <path d="M3 0 L770 6 Q792 8 792 28 L790 160 Q788 205 765 222 L0 243 Z"/>
      </clipPath>
      <radialGradient id="clover-tone" cx="50%" cy="50%" r="50%">
        <stop offset="0" stop-color="var(--lavender)"/>
        <stop offset="1" stop-color="var(--lavender-soft)"/>
      </radialGradient>
    </defs>

    <g clip-path="url(#window-shape)">
      <rect class="window-ground" x="0" y="0" width="800" height="245" fill="var(--teal)"/>

      <!-- wave bands -->
      <path class="wave-olive" d="M0 205 C150 150 300 165 430 195 C560 222 700 215 800 160 L800 245 L0 245 Z" fill="var(--olive)"/>
      <path class="wave-white" d="M0 192 C150 150 300 158 430 185 C560 210 700 205 800 150" fill="none" stroke="var(--white)" stroke-width="9"/>
      <path class="wave-white-thin" d="M20 238 C160 200 300 195 440 214 C580 232 700 222 800 190" fill="none" stroke="var(--white)" stroke-width="5"/>
      <path class="wave-olive-thin" d="M0 222 C150 185 300 182 430 203" fill="none" stroke="var(--olive-light)" stroke-width="3"/>
    </g>

    <!-- left brand: Fröhlich vital -->
    <g class="brand-block">
      <circle class="brand-mark" cx="40" cy="57" r="33" fill="var(--olive)"/>
      <text class="brand-kicker" x="202" y="43" text-anchor="middle">FRÖHLICH VITAL</text>
      <text class="brand-name" x="202" y="71" text-anchor="middle">MARLENE KOSTKA</text>
      <text class="brand-role" x="202" y="83" text-anchor="middle">HOLISTISCHE DARMTHERAPEUTIN UND COACH</text>
      <text class="brand-phone" x="20" y="118">Tel :  +49 0208 5539217</text>
      <text class="brand-web" x="20" y="140">www.fröhlich-vital-marlene-kostka.de</text>
    </g>

    <!-- course areas -->
    <g class="course-offers">
      <circle cx="425" cy="95" r="80" fill="url(#clover-tone)" role="img" aria-label="Kleeblatt-Illustration mit vier Kursbereichen"/>
      <text class="offer-label" x="424" y="36" text-anchor="middle">Für Frauen,</text>
      <text class="offer-label" x="424" y="45" text-anchor="middle">Schwangere</text>
      <text class="offer-label" x="424" y="55" text-anchor="middle">und Mütter</text>
      <text class="offer-label" x="468" y="91" text-anchor="middle">Für Babys</text>
      <text class="offer-label" x="468" y="100" text-anchor="middle">und Kinder</text>
      <text class="offer-label" x="381" y="96" text-anchor="middle">Kurse ab 60</text>
      <text class="offer-label" x="424" y="144" text-anchor="middle">Schwimmkurse</text>
    </g>

    <!-- right brand: Sonnenstunde -->
    <g class="practice-block">
      <text class="practice-name" x="630" y="52" text-anchor="middle">sonnenstunde</text>
      <text class="practice-tagline" x="630" y="76" text-anchor="middle">Die Kurspraxis</text>
      <text class="practice-intro" x="630" y="91" text-anchor="middle">Wir bieten folgende Kurse</text>
      <text class="practice-contact" x="630" y="118" text-anchor="middle">www.sonnenstunde-velmar.de</text>
      <text class="practice-contact" x="630" y="139" text-anchor="middle">46149 Oberhausen, Tel 0208/5539217</text>
      <text class="practice-contact" x="630" y="160" text-anchor="middle">anmeldung@sonnenstunde-velmar.de</text>
    </g>
  </svg>
</div>
</body>
</html>
```